Web Design Project

We are an online tax Continuing education provider. We provide online courses for tax preparers. We want the front end page to be user friendly and for the buyer to know exactly what they are looking at. We want a front end page to look smiliar www.marlowfiling.com. It should have a similar feel to this one.
Our website address will be www.7382QL.com
We currently have another website that is www.LedgerRJs.com but we do not want it to look like this. We want a different look but same information.
We have a logo already which is attached. We don't have specific colors in mind for the front page but don't want it to be too busy looking. It should stand out but not too simple either.
Target Market(s)
Tax Preparers. More serious and professional but these folks are usually not tech savy. Simple, easy to use, and functional is key.
Industry/Entity Type
Education
Requirements
Must have
- Use standard HTML & CSS. NO other coding is needed.
We are looking for 5-7 pages including Home page, log in, FAQ.
Please look at our current website www.LedgerRJs.com and also www.marlowfiling.com

```html
<!DOCTYPE html>
<html lang="en">
<head>
<meta charset="utf-8">
<title>7382QL – Continuing Education Made Simple</title>
<link rel="stylesheet" href="https://fonts.googleapis.com/css2?family=Fira+Sans:ital,wght@0,400;0,500;1,400&family=Arimo:wght@700&display=swap">
<style>
:root{
  --navy:#1b3157;
  --white:#fff;
  --ink:#333;
  --muted:#777;
  --title:#2e3f80;
  --orange:#f7941d;
  --nav-active:#fdbb6b;
  --green:#a4c639;
  --green-dark:#8db12a;
  --cyan:#1aa3cc;
  --red:#e0201b;
  --card:#f1f1f1;
  --card-line:#d6d6d6;
  --footer:#ebebeb;
  --check-blue:#2b9fe6;
  --check-green:#5ee41a;
  --check-orange:#f7941d;
}
*{margin:0;padding:0;box-sizing:border-box}
html,body{width:907px;height:1200px;overflow:hidden;background:var(--white)}
body{position:relative;font-family:"Fira Sans",sans-serif;color:var(--ink)}
.abs{position:absolute}

.brand{left:105px;top:30px;font-size:26px;font-weight:500;color:var(--title)}
.contact-line{right:108px;font-size:11px;color:var(--ink);display:flex;align-items:center;gap:6px}
.contact-line.addr{top:8px}
.contact-line.phone{top:29px}
.contact-line .num{color:var(--red)}
.nav{top:57px;left:458px;display:flex;font-size:12px;letter-spacing:.3px}
.nav a{display:block;height:26px;line-height:26px;padding:0 16px;color:var(--ink);text-decoration:none;margin-right:4px}
.nav a.active{background:var(--nav-active);color:var(--white);padding:0 14px}
.nav a.courses{margin-left:2px}
.nav a.faq{margin-left:4px}
.nav a.contact{margin-left:4px}
.nav a.signin{margin-left:4px}

.hero-band{left:0;top:92px;width:907px;height:329px;background:var(--navy)}
.hero-frame{left:106px;top:113px;width:694px;height:287px;background:var(--white)}
.hero{left:113px;top:120px;width:680px;height:273px;background:#000;overflow:hidden}
.hero-photo{position:absolute;right:0;top:0;width:430px;height:273px;background:linear-gradient(90deg,#000 0%,#2a2320 30%,#4a3a32 60%,#3a2a24 100%)}
.hero h1{position:absolute;left:22px;top:30px;font-weight:400;font-size:23px;color:var(--white)}
.checks{position:absolute;left:24px;top:74px;list-style:none}
.checks li{display:flex;align-items:center;gap:10px;font-size:19px;height:38.5px}
.checks .fast{color:var(--check-blue)}
.checks .easy{color:var(--check-green)}
.checks .cost{color:var(--check-orange)}
.hero .online{position:absolute;left:22px;top:197px;font-size:15px;color:var(--white)}

.card{top:449px;width:213px;height:329px;background:linear-gradient(#ececec,#f7f7f7);border:1px solid var(--card-line);border-radius:3px}
.card h2{position:absolute;left:13px;top:12px;width:195px;font-weight:400;font-size:15.5px;line-height:19.5px;color:var(--title)}
.card ul{position:absolute;left:13px;top:60px;width:195px;list-style:none;font-size:10.5px;line-height:13px}
.card li{position:relative;padding-left:14px;margin-bottom:8px}
.card li::before{content:"➪";position:absolute;left:0;top:0;font-size:8px;color:#999}
.price{left:58px;top:184px;width:94px;height:94px;border-radius:50%;background:var(--orange);color:var(--white);font-family:"Arimo",sans-serif;font-weight:700;font-size:24px;text-align:center;padding-top:25px}
.provider{left:21px;top:242px;width:175px;height:25px;border-radius:13px;background:linear-gradient(var(--green),var(--green-dark));font-size:10.5px;text-align:center;line-height:25px;color:var(--ink)}
.more{left:31px;top:281px;width:149px;height:31px;background:var(--cyan);color:var(--white);font-family:"Arimo",sans-serif;font-weight:700;font-size:14px;text-align:center;line-height:31px;border-radius:2px}

.rule{left:118px;width:675px;height:1px;background:linear-gradient(90deg,transparent,#ccc 20%,#ccc 80%,transparent)}
.quote{left:118px;top:822px;width:675px;text-align:center;font-style:italic;font-size:11px;line-height:15px;color:#444}
.quote cite{display:block;color:var(--red)}
.bulletin{left:298px;top:911px;width:311px;height:35px;background:var(--cyan);color:var(--white);font-size:15px;text-align:center;line-height:35px;border-radius:2px}
.irs-link{left:0;top:957px;width:907px;text-align:center;font-size:16px;color:#222}
.irs-link span{color:#999}

.footer{left:0;top:1009px;width:907px;height:138px;background:var(--footer)}
.foot-col{top:1034px;list-style:none;font-size:10px;line-height:18px;color:#555}
.foot-col.tight{line-height:12px}
.foot-col.tight li{margin-bottom:6px}
.foot-col.narrow{line-height:17px}

.bottom{top:1147px;left:0;width:907px;height:53px}
.accreditor{left:106px;top:1158px;display:flex;align-items:center;gap:6px;font-size:8px;line-height:9px;color:#777}
.badge-sq{width:32px;height:32px;background:#d9d9d9;border:2px solid #b5b5b5}
.copy{left:357px;top:1170px;font-size:10px;color:#555}
.seal{left:620px;top:1159px;width:60px;height:32px;background:#c9a24a;border-radius:3px}
.partner{left:694px;top:1162px;font-size:19px;font-weight:500;color:#1e7a2e}
</style>
</head>
<body>

<header>
  <div class="abs brand">7382QL</div>
  <div class="abs contact-line addr">48 Sample Lane, Townname, 204 Country
    <svg width="9" height="12" viewBox="0 0 9 12"><path d="M4.5 0A4.5 4.5 0 0 0 0 4.5C0 8 4.5 12 4.5 12S9 8 9 4.5A4.5 4.5 0 0 0 4.5 0Zm0 6.3a1.8 1.8 0 1 1 0-3.6 1.8 1.8 0 0 1 0 3.6Z" fill="#1b3157"/></svg>
  </div>
  <div class="abs contact-line phone">Call us directly : <span class="num">(012) 555.204.7781</span>
    <svg width="8" height="12" viewBox="0 0 8 12"><rect x=".7" y=".7" width="6.6" height="10.6" rx="1.2" fill="none" stroke="#1b3157" stroke-width="1.4"/><rect x="3" y="9" width="2" height="1" fill="#1b3157"/></svg>
  </div>
  <nav class="abs nav">
    <a class="active" href="#">HOME</a>
    <a class="courses" href="#">COURSES</a>
    <a class="faq" href="#">FAQ</a>
    <a class="contact" href="#">CONTACT</a>
    <a class="signin" href="#">SIGN IN</a>
  </nav>
</header>

<section class="abs hero-band"></section>
<div class="abs hero-frame"></div>
<section class="abs hero">
  <div class="hero-photo" role="img" aria-label="Photo of a smiling graduate in cap and gown with classmates behind"></div>
  <h1>Continuing Education Made Simple!</h1>
  <ul class="checks">
    <li class="fast"><svg width="22" height="20" viewBox="0 0 22 20"><rect x="1" y="3" width="15" height="15" fill="none" stroke="#fff" stroke-width="2"/><path d="M4 10l4 5L20 1" fill="none" stroke="#fff" stroke-width="3"/></svg>Fast</li>
    <li class="easy"><svg width="22" height="20" viewBox="0 0 22 20"><rect x="1" y="3" width="15" height="15" fill="none" stroke="#fff" stroke-width="2"/><path d="M4 10l4 5L20 1" fill="none" stroke="#fff" stroke-width="3"/></svg>Easy</li>
    <li class="cost"><svg width="22" height="20" viewBox="0 0 22 20"><rect x="1" y="3" width="15" height="15" fill="none" stroke="#fff" stroke-width="2"/><path d="M4 10l4 5L20 1" fill="none" stroke="#fff" stroke-width="3"/></svg>Low Cost</li>
  </ul>
  <p class="online">Completely Online! "Self-paced"</p>
</section>

<article class="abs card" style="left:106px">
  <h2>15-Hour Package for IRS Registered Tax-Preparer CE</h2>
  <ul>
    <li>Ethics (2 hrs CE Credit)</li>
    <li>Charitable Contributions 101<br>(3 hrs CE Credit)</li>
    <li>Earned Income Credit<br>(2 hrs CE Credit)</li>
    <li>Deducting Transportation Expenses<br>(2 hrs CE Credit)</li>
  </ul>
  <div class="abs price">$42</div>
  <div class="abs provider">Provided by Northgate Learning, LLC</div>
  <div class="abs more">FIND OUT MORE</div>
</article>

<article class="abs card" style="left:347px">
  <h2>RTRP Exam Prepration Course 10 CE Credit</h2>
  <ul>
    <li>10-HR RTRP Exam Simulator Course</li>
    <li>Study for the RTRP exam and receive CE credit at the same time.</li>
    <li>It is comprised of four full-length practice exams (120 questions each).</li>
    <li>The fourth exam attempts to mimic the actual IRS exam.</li>
  </ul>
  <div class="abs price">$79.99</div>
  <div class="abs provider">Provided by Northgate Learning, LLC</div>
  <div class="abs more">FIND OUT MORE</div>
</article>

<article class="abs card" style="left:588px">
  <h2>Combo Package RTRP Exam Prep Course &amp; CE</h2>
  <ul>
    <li>10-HR RTRP Exam Simulator Course</li>
    <li>Study for the RTRP exam and receive CE credit at the same time.</li>
    <li>It is comprised of four full-length practice exams (120 questions each).</li>
    <li>The fourth exam attempts to mimic the actual IRS exam.</li>
  </ul>
  <div class="abs price">$99.90</div>
  <div class="abs provider">Provided by Northgate Learning, LLC</div>
  <div class="abs more">FIND OUT MORE</div>
</article>

<div class="abs rule" style="top:806px"></div>
<blockquote class="abs quote">The class was very convenient because I work crazy hours ... the pace was great. I learned some laws that I wasn't aware of to help my clients. I highly recommend this course to others. Thank you!!<cite>- Dana.Ok</cite></blockquote>
<div class="abs rule" style="top:882px"></div>

<div class="abs bulletin">RTRP Test Candidate Information Bullrtin</div>
<svg class="abs" style="left:612px;top:926px" width="36" height="20" viewBox="0 0 36 20"><path d="M34 18C26 16 14 12 4 3" fill="none" stroke="#555" stroke-width="1" stroke-dasharray="2 2"/><path d="M2 1l8 1M2 1l1 7" fill="none" stroke="#555" stroke-width="1.2"/></svg>
<p class="abs irs-link">IRS Latest Information Link <span>( Click button to open IRS document or link)</span></p>

<footer>
  <div class="abs footer"></div>
  <ul class="abs foot-col" style="left:134px"><li>Home</li><li>Courses</li><li>FAQ</li><li>Contact</li><li>Sign In</li></ul>
  <ul class="abs foot-col" style="left:262px"><li>IRS Approved Provider</li><li>Certificate of Completion</li><li>Professional!</li><li>Self-paced Low Cost</li><li>Fast &amp; Easy Convenience</li></ul>
  <ul class="abs foot-col tight" style="left:455px"><li>15-Hour Package for IRS Registered<br>Tax-Preparer CE</li><li>RTRP Exam Prepration Course 10 CE<br>Credit</li><li>Combo Package RTRP Exam Prep<br>Course &amp; CE</li></ul>
  <ul class="abs foot-col narrow" style="left:683px"><li>Support</li><li>Privacy Policy</li><li>Terms &amp; Conditions</li><li>Contact</li></ul>

  <div class="abs accreditor"><span class="badge-sq"></span><span>APPROVED<br>CONTINUING EDUCATION<br>ACCREDITOR</span></div>
  <p class="abs copy">Copyright ©2013 7382QL. All rights reserved.</p>
  <div class="abs seal" role="img" aria-label="Secure site badge"></div>
  <div class="abs partner">LedgerRJs.com</div>
</footer>

</body>
</html>
```